Velvet Oaks rebranding my business with a new business card

I have my new logo and now I need a refresher on my business cards. I really want something fun and fresh. I like black background or anything to make the color pop.
Logo
Name: Velvet Oaks
Contact Info as stated below:
Mira Calloway
647-382-9164
Logo
Name: Velvet Oaks
Mira Calloway
647-382-9164
fb.me/VelvetOaksbyMira
Instagram: @VelvetOaksbyMira

Industry/Entity Type

Business

Contact Information for Business Card

double-sided. Logo on one side. Contact info on the other.

Requirements
Must have
• Logo
• Name: Velvet Oaks
• Contact Info as stated below:
• Mira Calloway
• 647-382-9164
• fb.me/VelvetOaksbyMira
• fb.me/VelvetOaksbyMira

```html
<!DOCTYPE html>
<html lang="en">
<head>
<meta charset="utf-8">
<title>Velvet Oaks – Business Card</title>
<link href="https://fonts.googleapis.com/css2?family=Open+Sans:wght@400;600&display=swap" rel="stylesheet">
<style>
  :root {
    --backdrop: #3a3a3c;
    --card: #2a2a2c;
    --card-edge: #1c1c1e;
    --ink: #d9d9d9;
    --ink-soft: #bdbdbd;
    --rose: #c98aa8;
    --rose-deep: #b56c8f;
    --logo-ink: #e6dcc8;
  }
  html, body {
    margin: 0;
    padding: 0;
    width: 1200px;
    height: 716px;
    overflow: hidden;
    background: var(--backdrop);
    font-family: "Open Sans", Arial, sans-serif;
  }
  .canvas {
    position: relative;
    width: 1200px;
    height: 716px;
  }
  .card {
    position: absolute;
    width: 540px;
    height: 310px;
    border-radius: 18px;
    background: var(--card);
    box-shadow: 0 6px 0 var(--card-edge), 0 14px 30px rgba(0,0,0,.45);
    overflow: hidden;
  }
  .card-front { left: 40px; top: 70px; }
  .card-back { left: 620px; top: 320px; }

  .front-rings { position: absolute; inset: 0; }
  .front-brand {
    position: absolute;
    left: 0; top: 0;
    width: 540px; height: 310px;
    display: flex; align-items: center; justify-content: center;
    font-size: 34px; font-weight: 600;
    color: var(--logo-ink);
    letter-spacing: 1px;
  }

  .holder-name {
    position: absolute;
    left: 34px; top: 128px;
    margin: 0;
    font-size: 30px; font-weight: 400;
    color: var(--ink);
  }
  .divider {
    position: absolute;
    left: 30px; right: 30px; top: 176px;
    height: 2px;
    background: var(--rose);
  }
  .contact-list {
    position: absolute;
    top: 190px;
    margin: 0; padding: 0;
    list-style: none;
    font-size: 16px;
    color: var(--ink-soft);
  }
  .contact-list li {
    display: flex; align-items: center; gap: 10px;
    height: 30px;
  }
  .contact-left { left: 34px; }
  .contact-right { right: 30px; text-align: right; }
  .contact-right li { justify-content: flex-end; }
  .icon { width: 14px; height: 14px; flex: none; }
  .icon-square { width: 12px; height: 12px; background: var(--rose-deep); border-radius: 2px; flex: none; }

  .back-brand {
    position: absolute;
    left: 355px; top: 25px;
    width: 140px; height: 140px;
    border-radius: 50%;
    border: 2px solid var(--rose);
    box-shadow: 0 0 14px rgba(201,138,168,.45);
    display: flex; align-items: center; justify-content: center;
    font-size: 17px; font-weight: 600;
    color: var(--logo-ink);
  }
</style>
</head>
<body>
<main class="canvas">

  <section class="card card-front" aria-label="Card front">
    <svg class="front-rings" width="540" height="310" viewBox="0 0 540 310" aria-hidden="true">
      <defs>
        <linearGradient id="ringGlow" x1="0" y1="1" x2="1" y2="0">
          <stop offset="0" stop-color="#5fc9b4"/>
          <stop offset="0.35" stop-color="#d6d06a"/>
          <stop offset="0.65" stop-color="#c87ab8"/>
          <stop offset="1" stop-color="#e0445a"/>
        </linearGradient>
      </defs>
      <g fill="none" stroke="url(#ringGlow)" stroke-width="2">
        <circle cx="270" cy="150" r="172"/>
        <circle cx="270" cy="150" r="178"/>
        <circle cx="270" cy="150" r="184"/>
      </g>
    </svg>
    <div class="front-brand">Velvet Oaks</div>
  </section>

  <section class="card card-back" aria-label="Card back">
    <h1 class="holder-name">Mira Calloway</h1>
    <div class="back-brand">Velvet Oaks</div>
    <div class="divider"></div>

    <ul class="contact-list contact-left">
      <li>
        <svg class="icon" viewBox="0 0 24 24" aria-hidden="true"><path fill="#b56c8f" d="M6.6 10.8a15 15 0 0 0 6.6 6.6l2.2-2.2a1 1 0 0 1 1-.25 11.4 11.4 0 0 0 3.6.57 1 1 0 0 1 1 1V20a1 1 0 0 1-1 1A17 17 0 0 1 3 4a1 1 0 0 1 1-1h3.5a1 1 0 0 1 1 1c0 1.25.2 2.45.57 3.57a1 1 0 0 1-.25 1z"/></svg>
        647-382-9164
      </li>
      <li><span class="icon-square"></span>fb.me/VelvetOaksbyMira</li>
    </ul>

    <ul class="contact-list contact-right">
      <li>velvetoaksbymira@inboxly.com
        <svg class="icon" viewBox="0 0 24 24" aria-hidden="true"><rect x="2" y="5" width="20" height="14" rx="2" fill="#b56c8f"/><path d="M3 6l9 7 9-7" fill="none" stroke="#2a2a2c" stroke-width="2"/></svg>
      </li>
      <li>@VelvetOaksbyMira<span class="icon-square"></span></li>
    </ul>
  </section>

</main>
</body>
</html>
```